Insert sheet for our Dog Food Package

We need an information sheet to go inn our pet food package, with branding, and information on ingredients, nutrition and feeding guidance. We will also need two additional items which will be a variation on the label design:
1) Label for package (detailed label about us and our food)
2) Label for outer shipping box (simple label for branding)
We will start with the information, insert page. The winning designer will then deliver the package and box labels as simplified versions of the same graphical theme.
I have attached samples of an earlier drafts of the insert piece. Please disregard the style, form and colors of the examples given. THEY ARE ONLY THERE TO SHOW WHAT INFORMATION SHOULD BE INCLUDED. All colors and style should be from our logo (attached). All graphics, font styles, and placement of elements need to be YOUR creative design - not a copy of the sample we gave. PLEASE READ THIS AND PLEASE DO NOT SUBMIT ANY VARIATION OF THE EXAMPLES!!!!!!!

Target Market(s)

Pet Owners

Industry/Entity Type

Pet Food

Colors
EB3D1F
EC4F4E
F09395
F8D3D4
FCEDEE

Requirements
Must have
• All new design. New colors (based in the palette of our logo), new graphics, new fonts, new placement of elements.
Should not have
• Please disregard the style, form and colors of the examples given. THEY ARE ONLY THERE TO SHOW WHAT INFORMATION SHOULD BE INCLUDED.

```html
<!DOCTYPE html>
<html lang="en">
<head>
<meta charset="utf-8">
<title>Kaviro – Insert Sheet</title>
<link rel="stylesheet" href="https://fonts.googleapis.com/css2?family=Bebas+Neue&family=Roboto+Condensed:wght@400;700&family=Montserrat:wght@600;700&display=swap">
<style>
:root{
  --surround:#d3d3d3;
  --paper:#ffffff;
  --red:#a81f18;
  --brown:#4a2014;
  --ink:#4a1f12;
}
*{margin:0;padding:0;box-sizing:border-box}
html,body{width:1200px;height:1200px;overflow:hidden;background:var(--surround)}
.sheet{position:absolute;left:185px;top:81px;width:831px;height:1038px;background:var(--paper);overflow:hidden;box-shadow:0 8px 14px rgba(0,0,0,.35);color:var(--ink);font-family:"Roboto Condensed",sans-serif}
.band-top{position:absolute;left:0;top:0;width:100%;height:50px;background:var(--red)}
.band-bottom{position:absolute;left:0;bottom:0;width:100%;height:44px;background:var(--brown)}
.brand{position:absolute;left:35px;top:150px;width:176px;display:flex;align-items:center;justify-content:center;gap:8px;font-family:"Roboto Condensed",sans-serif;font-weight:700;font-size:34px;color:var(--red);letter-spacing:2px}
.brand-dot{width:14px;height:14px;border-radius:50%;background:var(--red)}
.love-art{position:absolute;left:67px;top:283px;width:140px;height:164px;background:linear-gradient(180deg,var(--brown) 0 28%,var(--red) 28% 100%);border-radius:10px}
.story-title{position:absolute;left:268px;top:92px;font-family:"Bebas Neue",sans-serif;font-size:88px;line-height:1;color:var(--ink)}
.story-text{position:absolute;left:270px;top:180px;width:560px;font-size:19px;line-height:23.2px;color:var(--ink)}
.story-text span{display:block}
.panel{position:absolute;left:48px;width:258px;border:3px solid var(--ink);background:var(--paper);overflow:hidden}
.panel-head{font-family:"Montserrat",sans-serif;font-weight:700;font-size:11px;padding:7px 6px;border-bottom:3px solid var(--ink);white-space:nowrap}
.panel-title{font-family:"Montserrat",sans-serif;font-weight:700;font-size:12.5px;letter-spacing:2px;text-align:center;padding:8px 0 0}
.nutrition{top:452px;height:260px}
.nutrition .panel-title{height:39px;border-bottom:1px solid var(--ink)}
.analysis{width:100%;border-collapse:collapse;font-family:"Montserrat",sans-serif;font-weight:700;font-size:10px}
.analysis td{border:1px solid var(--ink);padding:4px 3px;height:22px}
.analysis tr td:first-child{border-left:none;padding-left:20px}
.analysis tr td:last-child{border-right:none;text-align:center}
.analysis .val{text-align:center}
.ingredients{padding:6px 10px 0 18px;font-size:13.6px;line-height:16.4px}
.feeding{top:725px;height:238px}
.feeding .panel-head{height:27px;padding:6px 6px 0}
.feeding .panel-title{font-size:11.5px;height:22px;padding-top:7px;line-height:14px}
.feed-cols{display:flex;justify-content:space-between;align-items:center;height:24px;font-family:"Montserrat",sans-serif;font-weight:600;font-size:8.5px;letter-spacing:1.6px;padding:0 16px;border-bottom:1px solid var(--ink)}
.feed-table{width:100%;border-collapse:collapse;table-layout:fixed;font-size:13px}
.feed-table td{padding:0 10px;line-height:16px;vertical-align:middle}
.feed-table tr + tr td{border-top:1px solid var(--ink)}
.feed-table td:first-child{border-right:1px solid var(--ink);width:129px}
.feed-table td:last-child{text-align:right;padding-right:16px}
.feed-table .row-single{height:29px}
.feed-table .row-triple{height:62px}
.feed-table .row-double{height:38px}
.feed-table .row-last{height:27px}
.dogs-art{position:absolute;left:367px;top:479px;width:528px;height:528px;border-radius:50%;background:linear-gradient(160deg,var(--red) 0 55%,var(--brown) 55% 100%)}
.dogs-base{position:absolute;left:470px;top:880px;width:361px;height:158px;background:var(--brown)}
</style>
</head>
<body>
<main class="sheet">
  <div class="band-top"></div>

  <div class="brand"><span class="brand-dot"></span>KAVIRO</div>
  <div class="love-art" role="img" aria-label="Hand lettering 'Prepared with love for Biscuit' over a red heart"></div>

  <h1 class="story-title">OUR STORY</h1>
  <div class="story-text">
    <span>We Revolutionized the industry. Not</span>
    <span>Formulated to meet a minimum standard, but to develop the maximum health of the whole dog.</span>
    <span>" We didn't just set about to create a food that will 'pass a minimum standard'. We set out to</span>
    <span>revolutionize the industry by creating a food that is designed with Super-foods, Wholesome Grains,</span>
    <span>and Powerful Oils to help your dog achieve their maximum health, happiness and longevity.'</span>
  </div>

  <section class="panel nutrition">
    <div class="panel-head">WE PREPARED THE BEST FOR BISCUIT •</div>
    <div class="panel-title">NUTRITIONAL INFORMATION</div>
    <table class="analysis">
      <tr><td>Protein:</td><td class="val">15%</td><td>Total Fat:</td><td>9.5%</td></tr>
      <tr><td>Crude Fiber:</td><td class="val">2.0%</td><td>Moisture:</td><td>72%</td></tr>
    </table>
    <p class="ingredients">Potassium Citrate, DiCalcium Phosphate, Calcium Carbonate, Garbanzo Beans, Choline Bitartrate, Taurine, Salt, Zinc Proteinate, Magnesium Oxide, Iron Proteinate, Vitamin B-12, Selenium, Niacin, Riboflavin, Calcium Panthothen-ate, Thiamine, Vitamin A, Vitamin D, Calcium Iodate, Vitamin B6, Folic Acid</p>
  </section>

  <section class="panel feeding">
    <div class="panel-head">HOW MUCH SHOULD I FEED BISCUIT?</div>
    <div class="panel-title">RECOMMENDED FEEDING PLAN</div>
    <div class="feed-cols"><span>APPROXIMATE WEIGHT</span><span>FULL MEAL</span></div>
    <table class="feed-table">
      <tr class="row-single"><td>&lt;20 lbs</td><td>110 g</td></tr>
      <tr class="row-triple"><td>20-29lbs<br>30-39 lbs<br>40-54 lbs</td><td>200 g<br>250 g<br>300 g</td></tr>
      <tr class="row-double"><td>55-69 lbs<br>70-85 lbs</td><td>350 g<br>400 g</td></tr>
      <tr class="row-last"><td>85+ lbs</td><td>500 g</td></tr>
    </table>
  </section>

  <div class="band-bottom"></div>
  <div class="dogs-art" role="img" aria-label="Illustration of a white dog and a brown puppy looking up inside a large red circle with falling petals"></div>
  <div class="dogs-base" role="img" aria-label="Brown puppy figure continuing to the bottom edge"></div>
</main>
</body>
</html>
```